Custom Mexican Train Dominos Scorecard

My wife and I regularly play Mexican Train dominos with our friends and family and would like to create a series of custom scorecards specific to our various groups that we play with. The idea would be to have them printed on pads or in notebooks that over time will hold a record of all of our games. Searching around on the web, the only "off the shelf" that I see are pretty plain and boring (see attached). We would love something with a fun and playful mid-century graphic feel to it. Can be a single color or more than one. We want to have the player names incorporated into the design, so for the first one the names would be Carla, Douglas, Ruth & Oliver. We will want a place to date each card and of course boxes to fill out the score. I have included a few examples of how the scorecard is basically laid out. Can be any size and can be done in landscape or portrait. I think I would just like the title to say "Domino Night" or potentially no title at all with just a fun domino graphic. Thank you!

Requirements
Must have
• Basic score layout
Nice to have
• nothing in particular
Should not have
• nothing in particular

```html
<!DOCTYPE html>
<html lang="en">
<head>
<meta charset="utf-8">
<title>Domino Night Scorecard</title>
<link rel="stylesheet" href="https://fonts.googleapis.com/css2?family=Rye&family=Questrial&display=swap">
<style>
  :root {
    --page-bg: #f6f7f9;
    --maroon: #43161a;
    --maroon-light: #5a2228;
    --band-black: #141414;
    --paper: #ffffff;
    --tint: #f6f0f1;
    --rule: #a9a9a9;
    --ink: #1b1b1b;
    --label: #f1ece6;
    --tile-gold: #c7a46a;
    --tile-gold-dark: #9c7a44;
    --train: #2b0f12;
  }
  * { box-sizing: border-box; margin: 0; padding: 0; }
  html, body { width: 1200px; height: 800px; overflow: hidden; background: var(--page-bg); }
  .canvas { position: relative; width: 1200px; height: 800px; }
  .scorecard {
    position: absolute; left: 331px; top: 20px;
    width: 782px; height: 1106px;
    transform: scale(0.687); transform-origin: 0 0;
    background: var(--paper);
    display: grid; grid-template-rows: 180px 926px;
  }
  .masthead { position: relative; background: var(--maroon); }
  .masthead__ornament {
    position: absolute; left: 200px; top: 0; width: 365px; height: 176px;
    background: radial-gradient(ellipse at center, var(--maroon-light) 0%, var(--maroon) 70%);
    border-radius: 40px;
  }
  .masthead__title {
    position: absolute; left: 0; width: 782px; top: 74px; text-align: center;
    font-family: "Rye", serif; font-size: 33px; color: #fff; letter-spacing: 0.5px;
  }
  .masthead__art {
    position: absolute; left: 605px; top: 28px; width: 160px; height: 102px;
    background: linear-gradient(180deg, #3a1317, var(--train));
    border-radius: 6px;
  }
  .sheet { display: grid; grid-template-columns: 237px 545px; }
  .legend, .scores {
    display: grid;
    grid-template-rows: 63px 56px 53px 53px 58px 52px 47px 46px 53px 53px 52px 52px 53px 52px 61px 70px 51px;
  }
  .legend { background: var(--maroon); }
  .legend__band {
    background: var(--band-black); color: var(--label);
    font-family: "Questrial", sans-serif; font-size: 21px;
    display: flex; align-items: center; justify-content: center;
  }
  .legend__band--sub { margin: 0; }
  .legend__row { display: flex; align-items: center; padding-left: 57px; gap: 22px; }
  .tile {
    width: 96px; height: 40px; border-radius: 20px;
    background: linear-gradient(180deg, #dcbf86, var(--tile-gold) 60%, var(--tile-gold-dark));
    display: flex; align-items: center; justify-content: center;
  }
  .tile__face {
    position: relative; width: 76px; height: 30px; background: #fff; border-radius: 4px;
  }
  .tile__face::after {
    content: ""; position: absolute; left: 37px; top: 4px; width: 1.5px; height: 22px; background: var(--ink);
  }
  .legend__value {
    width: 40px; text-align: center;
    font-family: "Rye", serif; font-size: 27px; color: #fff;
  }
  .scores {
    grid-template-columns: 76px 76px 76px 73px 65px 67px 64px 48px;
  }
  .cell { border-right: 1px solid var(--rule); border-bottom: 1px solid var(--rule); }
  .cell:nth-child(8n) { border-right: 0; }
  .cell--head {
    background: var(--tint);
    font-family: "Rye", serif; font-size: 15px; color: var(--ink);
    display: flex; align-items: center; justify-content: center;
  }
  .cell--total { background: var(--tint); border-top: 4px double #555; }
  .footer-note {
    grid-column: 1 / -1; position: relative;
  }
  .footer-note__date {
    position: absolute; right: 4px; bottom: 2px;
    font-family: "Questrial", sans-serif; font-size: 19px; color: var(--ink);
  }
  .footer-note__line {
    display: inline-block; width: 155px; border-bottom: 2px dotted var(--ink); margin-left: 4px;
  }
</style>
</head>
<body>
<div class="canvas">
  <article class="scorecard">
    <header class="masthead">
      <div class="masthead__ornament" role="img" aria-label="Decorative scrollwork framing the title"></div>
      <h1 class="masthead__title">Domino Night</h1>
      <div class="masthead__art" role="img" aria-label="Vintage steam locomotive illustration"></div>
    </header>
    <section class="sheet">
      <div class="legend">
        <div class="legend__band">Player's Name</div>
        <div class="legend__row"><span class="tile"><span class="tile__face"></span></span><span class="legend__value">12</span></div>
        <div class="legend__row"><span class="tile"><span class="tile__face"></span></span><span class="legend__value">11</span></div>
        <div class="legend__row"><span class="tile"><span class="tile__face"></span></span><span class="legend__value">10</span></div>
        <div class="legend__row"><span class="tile"><span class="tile__face"></span></span><span class="legend__value">9</span></div>
        <div class="legend__row"><span class="tile"><span class="tile__face"></span></span><span class="legend__value">8</span></div>
        <div class="legend__row"><span class="tile"><span class="tile__face"></span></span><span class="legend__value">7</span></div>
        <div class="legend__band legend__band--sub">Sub Total</div>
        <div class="legend__row"><span class="tile"><span class="tile__face"></span></span><span class="legend__value">6</span></div>
        <div class="legend__row"><span class="tile"><span class="tile__face"></span></span><span class="legend__value">5</span></div>
        <div class="legend__row"><span class="tile"><span class="tile__face"></span></span><span class="legend__value">4</span></div>
        <div class="legend__row"><span class="tile"><span class="tile__face"></span></span><span class="legend__value">3</span></div>
        <div class="legend__row"><span class="tile"><span class="tile__face"></span></span><span class="legend__value">2</span></div>
        <div class="legend__row"><span class="tile"><span class="tile__face"></span></span><span class="legend__value">1</span></div>
        <div class="legend__row"><span class="tile"><span class="tile__face"></span></span><span class="legend__value">0</span></div>
        <div class="legend__band">Game Total</div>
        <div></div>
      </div>
      <div class="scores">
        <div class="cell cell--head">Carla</div><div class="cell cell--head">Douglas</div><div class="cell cell--head">Ruth</div><div class="cell cell--head">Oliver</div><div class="cell cell--head"></div><div class="cell cell--head"></div><div class="cell cell--head"></div><div class="cell cell--head"></div>
        <div class="cell"></div><div class="cell"></div><div class="cell"></div><div class="cell"></div><div class="cell"></div><div class="cell"></div><div class="cell"></div><div class="cell"></div>
        <div class="cell"></div><div class="cell"></div><div class="cell"></div><div class="cell"></div><div class="cell"></div><div class="cell"></div><div class="cell"></div><div class="cell"></div>
        <div class="cell"></div><div class="cell"></div><div class="cell"></div><div class="cell"></div><div class="cell"></div><div class="cell"></div><div class="cell"></div><div class="cell"></div>
        <div class="cell"></div><div class="cell"></div><div class="cell"></div><div class="cell"></div><div class="cell"></div><div class="cell"></div><div class="cell"></div><div class="cell"></div>
        <div class="cell"></div><div class="cell"></div><div class="cell"></div><div class="cell"></div><div class="cell"></div><div class="cell"></div><div class="cell"></div><div class="cell"></div>
        <div class="cell"></div><div class="cell"></div><div class="cell"></div><div class="cell"></div><div class="cell"></div><div class="cell"></div><div class="cell"></div><div class="cell"></div>
        <div class="cell"></div><div class="cell"></div><div class="cell"></div><div class="cell"></div><div class="cell"></div><div class="cell"></div><div class="cell"></div><div class="cell"></div>
        <div class="cell"></div><div class="cell"></div><div class="cell"></div><div class="cell"></div><div class="cell"></div><div class="cell"></div><div class="cell"></div><div class="cell"></div>
        <div class="cell"></div><div class="cell"></div><div class="cell"></div><div class="cell"></div><div class="cell"></div><div class="cell"></div><div class="cell"></div><div class="cell"></div>
        <div class="cell"></div><div class="cell"></div><div class="cell"></div><div class="cell"></div><div class="cell"></div><div class="cell"></div><div class="cell"></div><div class="cell"></div>
        <div class="cell"></div><div class="cell"></div><div class="cell"></div><div class="cell"></div><div class="cell"></div><div class="cell"></div><div class="cell"></div><div class="cell"></div>
        <div class="cell"></div><div class="cell"></div><div class="cell"></div><div class="cell"></div><div class="cell"></div><div class="cell"></div><div class="cell"></div><div class="cell"></div>
        <div class="cell"></div><div class="cell"></div><div class="cell"></div><div class="cell"></div><div class="cell"></div><div class="cell"></div><div class="cell"></div><div class="cell"></div>
        <div class="cell"></div><div class="cell"></div><div class="cell"></div><div class="cell"></div><div class="cell"></div><div class="cell"></div><div class="cell"></div><div class="cell"></div>
        <div class="cell cell--total"></div><div class="cell cell--total"></div><div class="cell cell--total"></div><div class="cell cell--total"></div><div class="cell cell--total"></div><div class="cell cell--total"></div><div class="cell cell--total"></div><div class="cell cell--total"></div>
        <div class="footer-note"><span class="footer-note__date">Date:<span class="footer-note__line"></span></span></div>
      </div>
    </section>
  </article>
</div>
</body>
</html>
```